Web site for Tree Removal Company

What we are looking for:
-------------------------------
Looking for a wordpress web site, you can provide your own template or we can supply you with one (http://quorvel.plindatheme.net).

What we do
---------------
To see what we do please go to google Australia and google "Tree removal Sydney" or "Tree Removal Melbourne".

Web site requirements
-----------------------------
We prefer you to use our template as it has all our requirements in already.
- Responsive.
- Based on Wordpress.
- Full complaint and compatible with plugs.

Look, Feel and Appearance
------------------------------------
Please use the logo (see attached), for colour scheme, look and feel of the web site.

Thank you for your time and effort!

Target Market(s)

Tree Removal for Residential Homes

Industry/Entity Type

It Company

Number of Pages Required

4 page

Font styles to use
Serif
Sans Serif

Requirements
Must have
• Wordpress
Nice to have
• Original artwork, images and text
Should not have
• non related images or wording

```html
<!DOCTYPE html>
<html lang="en">
<head>
<meta charset="utf-8">
<title>Tavilow — Services</title>
<link rel="stylesheet" href="https://fonts.googleapis.com/css2?family=Mulish:wght@300;400;500;800;900&display=swap">
<style>
  :root {
    --ink: #000000;
    --paper: #ffffff;
    --accent: #ff6a13;
    --leaf: #6cc49a;
    --bark: #8a8a8a;
    --body-text: #1a1a1a;
  }
  * { box-sizing: border-box; margin: 0; padding: 0; }
  html, body { width: 1200px; height: 954px; overflow: hidden; background: var(--paper); }
  body { font-family: "Mulish", Arial, sans-serif; color: var(--ink); position: relative; }

  .site-header { position: absolute; left: 0; top: 0; width: 1200px; height: 127px; background: var(--ink); }
  .main-nav a {
    position: absolute; top: 48px; color: var(--paper); text-decoration: none;
    font-weight: 900; font-size: 17px; letter-spacing: 0.2px; text-transform: uppercase;
  }
  .main-nav .caret { display: inline-block; margin-left: 16px; font-size: 13px; }
  .nav-services { left: 61px; }
  .nav-locations { left: 234px; }
  .nav-about { left: 424px; }
  .nav-contact { left: 782px; }
  .quote-button {
    position: absolute; left: 946px; top: 37px; width: 193px; height: 46px;
    background: var(--accent); border-radius: 23px; color: var(--paper);
    font-weight: 900; font-size: 16px; text-transform: uppercase; text-decoration: none;
    display: flex; align-items: center; justify-content: center;
  }

  .brand-badge {
    position: absolute; left: 531px; top: -42px; width: 230px; height: 230px;
    border-radius: 50%; background: var(--ink);
    display: flex; flex-direction: column; align-items: center; justify-content: flex-end; padding-bottom: 34px;
  }
  .brand-badge .brand-dot { width: 80px; height: 80px; border-radius: 50%; background: var(--leaf); margin-bottom: 14px; }
  .brand-name { font-weight: 500; font-size: 22px; letter-spacing: 3px; color: var(--bark); text-transform: uppercase; }

  .call-line { position: absolute; left: 850px; top: 160px; width: 282px; text-align: right; }
  .call-line svg { position: absolute; left: 0; top: 0; }
  .call-main { font-size: 24px; font-weight: 400; line-height: 1; }
  .call-main .phone { color: var(--accent); font-weight: 800; }
  .call-sub { font-size: 24px; line-height: 1.05; padding-right: 6px; }

  .section-title { position: absolute; left: 59px; top: 224px; font-size: 43px; font-weight: 900; }

  .service { position: absolute; width: 330px; }
  .service h3 { font-size: 24px; font-weight: 500; margin-bottom: 14px; }
  .service p { font-size: 15.5px; font-weight: 300; line-height: 25px; letter-spacing: 0.1px; color: var(--body-text); }
  .col-left { left: 62px; }
  .col-right { left: 788px; }
  .row-1 { top: 327px; }
  .row-2 { top: 450px; }
  .row-3 { top: 575px; }

  .service-photo {
    position: absolute; left: 400px; top: 295px; width: 342px; height: 366px;
    background: radial-gradient(ellipse at 50% 45%, #e07a3a 0%, #c9a07a 22%, #d9d9d9 50%, #f4f4f4 78%, #ffffff 100%);
  }

  .site-footer { position: absolute; left: 0; top: 765px; width: 1200px; height: 189px; background: var(--ink); }
  .social { position: absolute; width: 31px; height: 31px; border-radius: 50%; background: var(--paper); }
  .footer-brand { position: absolute; left: 962px; top: 18px; width: 120px; display: flex; flex-direction: column; align-items: center; }
  .footer-brand .brand-dot { width: 92px; height: 92px; border-radius: 50%; background: var(--paper); margin-bottom: 10px; }
  .footer-brand .brand-name { color: var(--paper); font-size: 18px; }
</style>
</head>
<body>
  <header class="site-header">
    <nav class="main-nav">
      <a class="nav-services" href="#">Services<span class="caret">▼</span></a>
      <a class="nav-locations" href="#">Locations<span class="caret">▼</span></a>
      <a class="nav-about" href="#">About Us</a>
      <a class="nav-contact" href="#">Contact</a>
    </nav>
    <a class="quote-button" href="#">Get a free quote</a>
  </header>

  <div class="brand-badge">
    <span class="brand-dot"></span>
    <span class="brand-name">Tavilow</span>
  </div>

  <div class="call-line">
    <svg width="20" height="32" viewBox="0 0 20 32" aria-hidden="true">
      <rect x="1.5" y="1.5" width="17" height="29" rx="3" fill="none" stroke="#000" stroke-width="3"/>
      <rect x="4" y="5" width="12" height="19" fill="#000"/>
      <circle cx="10" cy="27" r="1.5" fill="#000"/>
    </svg>
    <div class="call-main">Call <span class="phone">+61 400 555 019</span></div>
    <div class="call-sub">for a free quote</div>
  </div>

  <main>
    <h1 class="section-title">Services</h1>

    <div class="service col-left row-1"><h3>Tree Removal</h3><p>Sed egestas, ante et vulputate volutpat,<br>eros pede semper est,</p></div>
    <div class="service col-left row-2"><h3>Mulching Services</h3><p>Sed egestas, ante et vulputate volutpat,<br>eros pede semper est,</p></div>
    <div class="service col-left row-3"><h3>Tree Pruning</h3><p>Sed egestas, ante et vulputate volutpat,<br>eros pede semper est,</p></div>

    <div class="service-photo" role="img" aria-label="Arborist in orange safety gear climbing between pale tree trunks"></div>

    <div class="service col-right row-1"><h3>Stump Removal</h3><p>Sed egestas, ante et vulputate volutpat,<br>eros pede semper est,</p></div>
    <div class="service col-right row-2"><h3>Hedge Trimming</h3><p>Sed egestas, ante et vulputate volutpat,<br>eros pede semper est,</p></div>
    <div class="service col-right row-3"><h3>Arborist Reports</h3><p>Sed egestas, ante et vulputate volutpat,<br>eros pede semper est,</p></div>
  </main>

  <footer class="site-footer">
    <a class="social" href="#" aria-label="Social link" style="left:904px; top:20px;"></a>
    <a class="social" href="#" aria-label="Social link" style="left:904px; top:66px;"></a>
    <a class="social" href="#" aria-label="Social link" style="left:905px; top:111px;"></a>
    <a class="social" href="#" aria-label="Social link" style="left:1108px; top:20px;"></a>
    <a class="social" href="#" aria-label="Social link" style="left:1108px; top:67px;"></a>
    <div class="footer-brand">
      <span class="brand-dot"></span>
      <span class="brand-name">Tavilow</span>
    </div>
  </footer>
</body>
</html>
```